PLM - Business Card Design Project

We need a business card based on our logo
Updates

Hi I just upload logo file in AI format Thanks and regards

Target Market(s)

Bank, Big companies, Business owners

Industry/Entity Type

Business

Font styles to use
Sans Serif

```html
<!DOCTYPE html>
<html lang="en">
<head>
<meta charset="utf-8">
<title>PLM – Business Card</title>
<link rel="stylesheet" href="https://fonts.googleapis.com/css2?family=Open+Sans:wght@400&display=swap">
<style>
  :root {
    --stage: #1d1d1f;
    --paper: #ffffff;
    --navy: #11284a;
    --slate: #7f9195;
    --light: #ffffff;
    --icon: #d9dde2;
  }
  html, body {
    margin: 0;
    width: 1200px;
    height: 927px;
    overflow: hidden;
    background: var(--stage);
    font-family: "Open Sans", sans-serif;
  }
  .card {
    position: absolute;
    left: 100px;
    top: 177px;
    width: 1000px;
    height: 572px;
    background: var(--paper);
    overflow: hidden;
  }
  .card-panels {
    position: absolute;
    inset: 0;
  }
  .brand {
    position: absolute;
    left: 70px;
    top: 240px;
    display: flex;
    align-items: center;
    gap: 18px;
    color: var(--navy);
  }
  .brand-mark {
    width: 52px;
    height: 52px;
    background: var(--navy);
  }
  .brand-name {
    margin: 0;
    font-size: 64px;
    font-weight: 400;
    line-height: 1;
  }
  .person {
    position: absolute;
    right: 32px;
    top: 38px;
    text-align: right;
    color: var(--light);
  }
  .person-name {
    margin: 0;
    font-size: 40px;
    font-weight: 400;
    line-height: 1.1;
  }
  .person-role {
    margin: 2px 0 0;
    font-size: 24px;
    line-height: 1.1;
  }
  .contacts {
    position: absolute;
    right: 28px;
    top: 428px;
    margin: 0;
    padding: 0;
    list-style: none;
    color: var(--light);
    font-size: 23px;
    line-height: 34px;
    text-align: right;
  }
  .contacts li {
    display: flex;
    justify-content: flex-end;
    align-items: center;
    gap: 10px;
  }
  .contact-icon {
    width: 16px;
    height: 16px;
    fill: var(--icon);
  }
</style>
</head>
<body>
  <article class="card">
    <svg class="card-panels" width="1000" height="572" viewBox="0 0 1000 572" aria-hidden="true">
      <polygon points="343,0 396,0 610,572 600,572" fill="var(--slate)"/>
      <polygon points="396,0 1000,0 1000,572 610,572" fill="var(--navy)"/>
    </svg>

    <div class="brand">
      <span class="brand-mark" aria-hidden="true"></span>
      <p class="brand-name">PLM</p>
    </div>

    <div class="person">
      <p class="person-name">MARC TANNER</p>
      <p class="person-role">DIRECTOR</p>
    </div>

    <ul class="contacts">
      <li>+65 5550 1834
        <svg class="contact-icon" viewBox="0 0 16 16" aria-hidden="true"><path d="M1 6c0-2 3-3.5 7-3.5S15 4 15 6v1.5h-3.5V6h-7v1.5H1z"/><path d="M4 8h8l2 5H2z"/></svg>
      </li>
      <li>info@cabinetlemaire.com
        <svg class="contact-icon" viewBox="0 0 16 16" aria-hidden="true"><path d="M2 4h12v8H2z M2 4l6 5 6-5" stroke="var(--navy)" stroke-width="1"/></svg>
      </li>
      <li>www.cabinetlemaire.com
        <svg class="contact-icon" viewBox="0 0 16 16" aria-hidden="true"><circle cx="8" cy="8" r="6.5"/><path d="M1.5 8h13M8 1.5v13M3 4.5h10M3 11.5h10" stroke="var(--navy)" stroke-width="0.8" fill="none"/><ellipse cx="8" cy="8" rx="3" ry="6.5" stroke="var(--navy)" stroke-width="0.8" fill="none"/></svg>
      </li>
    </ul>
  </article>
</body>
</html>
```